I need book cover graphics for 2/4 short pdf monographs
Titles:
1. Can Gardeners Really Outlast Winter Frost?
Hard Lessons Regarding Soil and Seasons
2. 7 Tricks every Orchard Keeper Quietly Hides
I want to use the same/similar cover design a second time for Plastic (Cosmetic) Surgery so the covers should be generic medical, perhaps with some images reference to beauty in the case or Plastic Surgery and weight loss in the case of Bariatric Surgery. You would just change the title block to refer to the other specialty, substituting Cosmetic for Weight Loss and Plastic for Bariatric.
Size is 6"x9" or A5

```html
<!DOCTYPE html>
<html lang="en">
<head>
<meta charset="UTF-8">
<title>Can Gardeners Really Outlast Winter Frost? – Cover</title>
<link href="https://fonts.googleapis.com/css2?family=Bebas+Neue&display=swap" rel="stylesheet">
<style>
  :root {
    --scrub-dark: #2a463f;
    --scrub-mid: #46705f;
    --scrub-light: #6e9587;
    --steel-glint: rgba(214, 214, 206, 0.75);
    --steel-shadow: rgba(70, 72, 70, 0.55);
    --skin-warm: rgba(176, 140, 118, 0.8);
    --skin-shade: rgba(120, 92, 78, 0.7);
    --backdrop-grey: #c8cbc7;
    --band-amber: #f6aa1c;
    --title-steel-light: #b4b4b2;
    --title-steel-dark: #5f5f5f;
    --subtitle-white: #ffffff;
  }
  html, body {
    margin: 0;
    padding: 0;
    width: 846px;
    height: 1200px;
    overflow: hidden;
    background: #ffffff;
  }
  .cover {
    position: relative;
    width: 846px;
    height: 1200px;
    overflow: hidden;
    font-family: "Bebas Neue", "Oswald", sans-serif;
  }
  .cover-photo {
    position: absolute;
    inset: 0;
    background:
      radial-gradient(ellipse 16% 10% at 60% 42%, var(--skin-warm), rgba(176,140,118,0) 100%),
      radial-gradient(ellipse 14% 14% at 72% 30%, var(--skin-shade), rgba(120,92,78,0) 100%),
      radial-gradient(ellipse 12% 6% at 30% 52%, rgba(176,140,118,0.55), rgba(176,140,118,0) 100%),
      radial-gradient(ellipse 28% 22% at 42% 38%, var(--steel-glint), rgba(214,214,206,0) 100%),
      radial-gradient(ellipse 22% 16% at 66% 56%, rgba(200,196,184,0.6), rgba(200,196,184,0) 100%),
      radial-gradient(ellipse 18% 10% at 62% 80%, rgba(170,160,140,0.5), rgba(170,160,140,0) 100%),
      radial-gradient(ellipse 30% 30% at 40% 46%, var(--steel-shadow), rgba(70,72,70,0) 100%),
      linear-gradient(90deg, rgba(0,0,0,0) 80%, var(--backdrop-grey) 100%),
      linear-gradient(160deg, var(--scrub-light) 0%, var(--scrub-mid) 40%, var(--scrub-dark) 100%);
  }
  .title-band {
    position: absolute;
    left: 0;
    top: 662px;
    width: 846px;
    height: 220px;
    background: var(--band-amber);
  }
  .title {
    position: absolute;
    left: 40px;
    top: 676px;
    width: 800px;
    margin: 0;
    text-align: left;
    font-weight: 400;
    font-size: 100px;
    line-height: 85px;
    letter-spacing: 1px;
    background: linear-gradient(180deg, var(--title-steel-light) 0%, var(--title-steel-dark) 100%);
    -webkit-background-clip: text;
    background-clip: text;
    color: transparent;
  }
  .title-line { display: block; white-space: nowrap; }
  .subtitle {
    position: absolute;
    left: 0;
    top: 897px;
    width: 846px;
    margin: 0;
    text-align: center;
    font-weight: 400;
    font-size: 52px;
    line-height: 56px;
    letter-spacing: 1px;
    white-space: nowrap;
    color: var(--subtitle-white);
    text-shadow: 1px 2px 3px rgba(0,0,0,0.6);
  }
</style>
</head>
<body>
  <main class="cover">
    <div class="cover-photo" role="img" aria-label="Close-up of a person in green scrubs holding a bundle of steel surgical instruments"></div>
    <div class="title-band"></div>
    <h1 class="title">
      <span class="title-line">Can Gardeners Really</span>
      <span class="title-line">Outlast Winter Frost?</span>
    </h1>
    <p class="subtitle">Hard Lessons Regarding Soil and Seasons</p>
  </main>
</body>
</html>
```